Flyer-Design für Fusspflege für den Mann
schade dass die Daten nicht auch im psd-format geliefert werden konnten
Zielgruppe
Fusspflege und Maniküre für den Mann - neu und zusammen in einem Haarentfernungsinstitut für Männer in Zürich
Aufgabenstellung
Sie haben freie Wahl - Farben an das Logo angepasst.
Für tolle Bilder bin ich offen.
Sollte auch stehen: nur auf Voranmeldung - am besten per SMS
Zudem das persönliche Foto dazu

```html
<!DOCTYPE html>
<html lang="de">
<head>
<meta charset="utf-8">
<title>Nur für Männer – Maniküre & Fusspflege</title>
<link rel="stylesheet" href="https://fonts.googleapis.com/css2?family=Poppins:ital,wght@0,400;0,500;0,700;0,800;0,900;1,800;1,900&display=swap">
<style>
  :root {
    --gold: #d9a632;
    --ink: #111111;
    --white: #ffffff;
  }
  html, body {
    margin: 0;
    padding: 0;
    overflow: hidden;
    background: #ffffff;
  }
  .flyer {
    position: relative;
    width: 848px;
    height: 1200px;
    overflow: hidden;
    font-family: "Poppins", sans-serif;
  }
  .flyer-photo {
    position: absolute;
    inset: 0;
  }
  .headline {
    position: absolute;
    left: 0;
    top: 0;
    width: 848px;
    height: 280px;
  }
  .headline text {
    font-family: "Poppins", sans-serif;
    font-weight: 900;
    fill: var(--gold);
    stroke: #2a2a2a;
    stroke-width: 7px;
    paint-order: stroke;
    stroke-linejoin: round;
  }
  .services {
    position: absolute;
    left: 0;
    top: 0;
    margin: 0;
    font-style: italic;
    font-weight: 800;
    color: var(--white);
  }
  .service {
    position: absolute;
    white-space: nowrap;
    font-size: 45px;
    line-height: 1;
    letter-spacing: 0.5px;
  }
  .service-manicure { left: 133px; top: 396px; }
  .service-foot { left: 176px; top: 496px; }
  .service-amp {
    position: absolute;
    left: 243px;
    top: 450px;
    font-size: 40px;
    font-style: normal;
    font-weight: 800;
    color: var(--gold);
    line-height: 1;
  }
  .booking-band {
    position: absolute;
    left: 0;
    top: 800px;
    width: 848px;
    height: 120px;
  }
  .booking-note {
    position: absolute;
    left: 42px;
    top: 823px;
    margin: 0;
    font-size: 19px;
    line-height: 25px;
    font-weight: 500;
    color: var(--ink);
    text-transform: uppercase;
  }
  .booking-note strong { font-weight: 800; }
  .booking-phone {
    position: absolute;
    left: 398px;
    top: 826px;
    margin: 0;
    font-size: 59px;
    line-height: 1;
    font-style: italic;
    font-weight: 800;
    color: var(--ink);
    letter-spacing: 0;
    white-space: nowrap;
  }
  .brand {
    position: absolute;
    left: 323px;
    top: 1030px;
    width: 200px;
    text-align: center;
  }
  .brand-dot {
    width: 22px;
    height: 22px;
    border-radius: 50%;
    background: var(--gold);
    margin: 0 auto 14px;
  }
  .brand-name {
    margin: 0;
    font-size: 44px;
    line-height: 1.1;
    font-weight: 500;
    color: var(--white);
  }
  .portrait {
    position: absolute;
    left: 643px;
    top: 934px;
    width: 166px;
    height: 166px;
  }
  .address {
    position: absolute;
    left: 42px;
    top: 1066px;
    margin: 0;
    font-style: normal;
    font-size: 19px;
    line-height: 27.5px;
    font-weight: 400;
    color: var(--white);
  }
  .address strong { font-weight: 700; }
  .contact {
    position: absolute;
    right: 42px;
    top: 1120px;
    margin: 0;
    text-align: right;
    font-size: 19px;
    line-height: 27px;
    font-weight: 500;
    color: var(--white);
  }
</style>
</head>
<body>
<main class="flyer">

  <svg class="flyer-photo" width="848" height="1200" viewBox="0 0 848 1200" role="img" aria-label="Foto: Mann in weissem Hemd, schwarzer Hose und Lackschuhen sitzt auf Steinstufen, gepflegte Hände auf dem Knie">
    <defs>
      <linearGradient id="photoTone" x1="0.1" y1="0" x2="0" y2="1">
        <stop offset="0" stop-color="#e9ebea"/>
        <stop offset="0.16" stop-color="#d6d8d6"/>
        <stop offset="0.3" stop-color="#5b5c59"/>
        <stop offset="0.4" stop-color="#232323"/>
        <stop offset="0.52" stop-color="#2a2a29"/>
        <stop offset="0.64" stop-color="#76776f"/>
        <stop offset="0.78" stop-color="#9d9e95"/>
        <stop offset="1" stop-color="#98876e"/>
      </linearGradient>
    </defs>
    <rect width="848" height="1200" fill="url(#photoTone)"/>
  </svg>

  <svg class="headline" viewBox="0 0 848 280" aria-labelledby="headline-title">
    <title id="headline-title">Nur für Männer</title>
    <text x="298" y="112" font-size="60" transform="rotate(-3 298 112)">NUR FÜR</text>
    <text x="96" y="246" font-size="142" transform="rotate(-3 96 246)" textLength="560" lengthAdjust="spacingAndGlyphs">MÄNNER</text>
  </svg>

  <h2 class="services">
    <span class="service service-manicure">MANIKÜRE</span>
    <span class="service-amp">&amp;</span>
    <span class="service service-foot">FUSSPFLEGE</span>
  </h2>

  <svg class="booking-band" viewBox="0 0 848 120" aria-hidden="true">
    <polygon points="0,2 848,16 848,106 0,116" fill="var(--gold)"/>
  </svg>
  <p class="booking-note">
    <strong>Termine nur nach</strong><br>
    <strong>Voranmeldung</strong> – am besten<br>
    per WhatsApp oder SMS
  </p>
  <p class="booking-phone">078 000 12 34</p>

  <div class="brand">
    <div class="brand-dot"></div>
    <p class="brand-name">NovaPed</p>
  </div>

  <svg class="portrait" viewBox="0 0 166 166" role="img" aria-label="Porträtfoto des Inhabers Luca Brandt">
    <defs>
      <radialGradient id="portraitTone" cx="0.5" cy="0.45" r="0.6">
        <stop offset="0" stop-color="#8a8a8a"/>
        <stop offset="1" stop-color="#1e1e1e"/>
      </radialGradient>
    </defs>
    <circle cx="83" cy="83" r="83" fill="url(#portraitTone)"/>
  </svg>

  <address class="address">
    <strong>NovaPed by Glattwerk</strong><br>
    Luca Brandt<br>
    Seefeldweg 14<br>
    CH - 8008 Zürich
  </address>

  <p class="contact">
    www.glattwerk.ch<br>
    luca@glattwerk.ch
  </p>

</main>
</body>
</html>
```